Fastest Work at home Solution for Small Businesses

We need a web page for a product called *CopperVale*
We develop an innovative VPN Appliance (Model-Name ->Vale Nine) that gives small business the possibility literally setup the possibility for Companies to let their employees work from home.
With our secure appliance we create safe connection between any business and the employee *working at home*
Our Products *Vale Nine* are rolled out in minutes.
A. Employees can connect directly
B. Work from any location
C. All this without having to change the company firewall
Use case
=======
1. Go to our page
2. Select Product
3. Order
4. Connect to any Switch in the company
5. install software on employees laptop
***** INSTANT Connection ******
Businesses

```html
<!DOCTYPE html>
<html lang="en">
<head>
<meta charset="utf-8">
<title>CopperVale – Fastest Work at home Solution for Small Businesses</title>
<link href="https://fonts.googleapis.com/css2?family=Jost:wght@400;500;600&family=Poppins:wght@400;500&display=swap" rel="stylesheet">
<style>
:root{
  --blue:#1f5fe0;
  --sky:#3cb6f2;
  --navy:#0b2c9e;
  --navy-deep:#082687;
  --ink:#1c2a6b;
  --text:#6c7088;
  --line:#d7dbe6;
  --grey-bg:#eeeff2;
  --white:#ffffff;
}
*{margin:0;padding:0;box-sizing:border-box}
html,body{width:1200px;height:4872px;overflow:hidden;background:var(--white)}
body{position:relative;font-family:"Poppins",sans-serif;color:var(--text)}
.abs{position:absolute}
h1,h2,h3,.brand,.nav a,.btn{font-family:"Jost",sans-serif}
p{font-size:15px;line-height:27px}

/* header */
.site-header{left:0;top:0;width:1200px;height:128px}
.brand{display:flex;align-items:center;gap:14px;font-weight:600;font-size:40px;color:var(--navy)}
.brand-mark{width:30px;height:30px;background:var(--blue)}
.site-header .brand{position:absolute;left:112px;top:38px}
.nav{position:absolute;right:110px;top:52px;display:flex;gap:44px}
.nav a{font-size:18px;color:var(--ink);text-decoration:none}
.nav a.active{color:var(--blue);font-weight:500}

/* hero */
.hero{left:0;top:128px;width:1200px;height:740px}
.hero-photo{position:absolute;inset:0;background:linear-gradient(135deg,#8c8a86 0%,#5a5c62 45%,#3d4048 70%,#6b6e76 100%)}
.hero h1{position:absolute;left:720px;top:418px;color:var(--white);font-weight:500;font-size:34px;line-height:52px}

/* products */
.section-title{width:1200px;text-align:center;font-size:56px;font-weight:600;color:var(--blue)}
.section-title span{color:var(--sky)}
.product-art{border-radius:12px;background:linear-gradient(135deg,#e8edfb,#d5dcf6 60%,#f6d6df)}
.product h3{font-size:30px;font-weight:500;color:var(--blue);line-height:38px}
.product p{width:490px;margin-top:30px}
.btn{display:inline-block;font-size:15px;border-radius:30px;text-decoration:none}
.btn-outline{margin-top:26px;width:158px;height:54px;line-height:52px;text-align:center;border:2px solid var(--sky);color:var(--blue)}
.btn-solid{background:var(--sky);color:var(--white);width:150px;height:54px;line-height:54px;text-align:center}
.btn-navy{background:var(--navy);color:var(--white);width:170px;height:56px;line-height:56px;text-align:center}

/* promo band */
.promo{left:0;top:2112px;width:1200px;height:500px;background:linear-gradient(100deg,#1246d6 0%,#2a78ea 45%,#5ab6f0 100%)}
.promo-photo{position:absolute;left:560px;top:0;width:640px;height:500px;background:linear-gradient(120deg,rgba(120,170,240,.45),rgba(160,210,250,.7))}
.promo h2{position:absolute;left:112px;top:114px;color:var(--white);font-size:32px;font-weight:500;line-height:44px}
.promo p{position:absolute;left:112px;top:222px;width:470px;color:#dce8ff;font-size:14px;line-height:24px}
.promo .btn{position:absolute;left:112px;top:330px}

/* steps */
.steps{left:0;top:2620px;width:1200px;height:660px;background:var(--grey-bg)}
.steps h2{position:absolute;top:54px;width:1200px;text-align:center;font-size:44px;font-weight:500;color:var(--blue);letter-spacing:1px}
.step{position:absolute;width:240px;height:240px}
.step-box{position:absolute;left:50%;top:50%;width:170px;height:170px;margin:-85px 0 0 -85px;border:3px solid #c8ccd6;border-radius:22px;transform:rotate(45deg);background:var(--grey-bg)}
.step-body{position:absolute;inset:0;display:flex;flex-direction:column;align-items:center;justify-content:center;gap:16px;text-align:center}
.step-body b{font-family:"Jost",sans-serif;font-size:14px;font-weight:600;color:var(--ink);line-height:18px}

/* anywhere */
.anywhere{left:0;top:3288px;width:1200px;height:492px}
.anywhere-photo{position:absolute;left:0;top:0;width:600px;height:492px;background:linear-gradient(135deg,#b9b3aa,#6b6a6c 55%,#3a3c44)}
.anywhere-panel{position:absolute;left:600px;top:0;width:600px;height:492px;background:var(--sky)}
.anywhere h2{position:absolute;left:48px;top:96px;color:var(--navy);font-size:26px;font-weight:500}
.anywhere p{position:absolute;left:48px;top:150px;width:500px;color:var(--white);font-size:14px;line-height:24px}
.anywhere .btn{position:absolute;left:48px;top:330px}

/* faq */
.faq{left:0;top:3800px;width:1200px;height:520px}
.faq h2{position:absolute;top:40px;width:1200px;text-align:center;font-size:52px;font-weight:500;color:var(--blue)}
.faq-decor{position:absolute;border-radius:14px;background:linear-gradient(135deg,rgba(31,95,224,.10),rgba(60,182,242,.16))}
.faq-item{position:absolute;left:200px;width:800px;height:54px;background:var(--white);border-radius:10px;box-shadow:0 4px 16px rgba(20,40,120,.14);display:flex;align-items:center;justify-content:space-between;padding:0 20px 0 26px;font-size:15px;color:var(--ink)}
.faq-toggle{width:22px;height:22px;border-radius:50%;background:var(--sky);color:var(--white);font-size:13px;line-height:22px;text-align:center}

/* footer */
.site-footer{left:0;top:4320px;width:1200px;height:552px;background:var(--navy)}
.footer-bottom{position:absolute;left:0;top:400px;width:1200px;height:152px;background:var(--navy-deep)}
.site-footer .brand{position:absolute;left:112px;top:84px;color:var(--white)}
.site-footer .brand-mark{background:var(--sky)}
.footer-about{position:absolute;left:112px;top:156px;width:300px;color:#c7d3ff;font-size:13px;line-height:22px}
.footer-col h3{font-size:20px;font-weight:500;color:var(--white);letter-spacing:.5px}
.contact-list{margin-top:26px;list-style:none}
.contact-list li{display:flex;gap:14px;color:#c7d3ff;font-size:13px;line-height:20px;margin-bottom:22px}
.contact-list svg{flex:none;margin-top:2px}
.footer-col .sub{margin-top:22px;width:330px;color:#c7d3ff;font-size:13px;line-height:22px}
.email-field{margin-top:22px;width:330px;height:46px;background:var(--white);font-size:13px;color:#8b90a6;padding:0 16px;line-height:46px}
.footer-col .btn-solid{margin-top:16px;width:140px;height:40px;line-height:40px;font-size:13px}
.socials{position:absolute;left:0;top:30px;width:1200px;display:flex;justify-content:center;gap:14px}
.socials span{width:34px;height:34px;border-radius:50%;border:2px solid #c7d3ff}
.copyright{position:absolute;left:0;top:92px;width:1200px;text-align:center;color:#c7d3ff;font-size:14px}
</style>
</head>
<body>

<header class="abs site-header">
  <div class="brand"><span class="brand-mark"></span>CopperVale</div>
  <nav class="nav">
    <a class="active" href="#">Home</a><a href="#">About Us</a><a href="#">Products</a><a href="#">How it work</a><a href="#">Blog</a><a href="#">Contact Us</a>
  </nav>
</header>

<section class="abs hero">
  <div class="hero-photo" role="img" aria-label="Photo of a woman working at home on a laptop on a sofa"></div>
  <svg class="abs" style="left:0;top:0" width="1200" height="740" viewBox="0 0 1200 740">
    <path d="M0 660 Q600 750 1200 560 L1200 740 L0 740 Z" fill="#ffffff"/>
    <path d="M640 700 Q950 660 1200 560 L1200 690 Q980 720 640 700 Z" fill="#3cb6f2"/>
  </svg>
  <h1>Fastest Work at home<br>Solution for Small Businesses</h1>
</section>

<h2 class="abs section-title" style="top:868px">Our <span>Products</span></h2>

<svg class="abs" style="left:0;top:1200px" width="1200" height="700" viewBox="0 0 1200 700">
  <path d="M300 60 Q310 190 500 200 Q830 210 880 170" fill="none" stroke="#b7bfd4" stroke-width="3" stroke-dasharray="3 9" stroke-linecap="round"/>
  <path d="M900 430 Q880 520 620 520 Q330 520 320 570" fill="none" stroke="#b7bfd4" stroke-width="3" stroke-dasharray="3 9" stroke-linecap="round"/>
</svg>

<div class="abs product-art" style="left:176px;top:980px;width:270px;height:260px" role="img" aria-label="Illustration of employees connecting to the office from their desks"></div>
<article class="abs product" style="left:500px;top:1000px">
  <h3>Employees can connect directly</h3>
  <p>Sed ut perspiciatis unde omnis iste natus error sit voluptatem accusantiu doloremque laudantium, totam rem aperiam, eaque ipsa quae ab illo in vent et quasi architecto beatae vitae dicta sunt explicabo.</p>
  <a class="btn btn-outline" href="#">Read More</a>
</article>

<article class="abs product" style="left:196px;top:1418px">
  <h3>Work from any location</h3>
  <p>Sed ut perspiciatis unde omnis iste natus error sit voluptatem accusantiu doloremque laudantium, totam rem aperiam, eaque ipsa quae ab illo in vent et quasi architecto beatae vitae dicta sunt explicabo.</p>
  <a class="btn btn-outline" href="#">Read More</a>
</article>
<div class="abs product-art" style="left:790px;top:1360px;width:280px;height:290px" role="img" aria-label="Illustration of people working from different locations linked together"></div>

<div class="abs product-art" style="left:176px;top:1760px;width:260px;height:290px" role="img" aria-label="Illustration of a person working on a laptop behind a firewall"></div>
<article class="abs product" style="left:500px;top:1756px">
  <h3>All this without having to change the<br>company firewall</h3>
  <p>Sed ut perspiciatis unde omnis iste natus error sit voluptatem accusantiu doloremque laudantium, totam rem aperiam, eaque ipsa quae ab illo in vent et quasi architecto beatae vitae dicta sunt explicabo.</p>
  <a class="btn btn-outline" href="#">Read More</a>
</article>

<section class="abs promo">
  <div class="promo-photo" role="img" aria-label="Photo of a person typing on a laptop, tinted blue"></div>
  <h2>Sed ut perspiciatis unde<br>iste natus error sit voluptatem accusan</h2>
  <p>Nemo enim ipsam voluptatem quia voluptas sit aspernatur aut odit aut fugit, sed quia consequuntur magni dolores eos qui ratione voluptatem sequi nesciunt neque porro.</p>
  <a class="btn btn-solid" href="#">Read More</a>
</section>

<section class="abs steps">
  <h2>HOW A VPN WORKS</h2>
  <div class="step" style="left:180px;top:120px">
    <div class="step-box"></div>
    <div class="step-body">
      <svg width="40" height="40" viewBox="0 0 40 40"><path d="M4 18 L36 4 L26 36 L19 22 Z" fill="#0b2c9e"/></svg>
      <b>GO TO OUR PAGE</b>
    </div>
  </div>
  <div class="step" style="left:520px;top:120px">
    <div class="step-box"></div>
    <div class="step-body">
      <svg width="40" height="40" viewBox="0 0 40 40"><rect x="8" y="4" width="24" height="32" rx="2" fill="none" stroke="#0b2c9e" stroke-width="3"/><path d="M13 13h14M13 20h14M13 27h9" stroke="#0b2c9e" stroke-width="3"/></svg>
      <b>ORDER</b>
    </div>
  </div>
  <div class="step" style="left:860px;top:120px">
    <div class="step-box"></div>
    <div class="step-body">
      <svg width="40" height="40" viewBox="0 0 40 40"><rect x="4" y="6" width="32" height="22" rx="2" fill="#0b2c9e"/><path d="M20 10v12M15 17l5 5 5-5" stroke="#fff" stroke-width="3" fill="none"/><rect x="2" y="30" width="36" height="4" fill="#0b2c9e"/></svg>
      <b>INSTALL SOFTWARE ON<br>EMPLOYEES LAPTOP</b>
    </div>
  </div>
  <div class="step" style="left:350px;top:340px">
    <div class="step-box"></div>
    <div class="step-body">
      <svg width="40" height="40" viewBox="0 0 40 40"><path d="M6 14h28v20H6z" fill="none" stroke="#0b2c9e" stroke-width="3"/><path d="M14 14v-6h12v6" fill="none" stroke="#0b2c9e" stroke-width="3"/></svg>
      <b>SELECT PRODUCT</b>
    </div>
  </div>
  <div class="step" style="left:690px;top:340px">
    <div class="step-box"></div>
    <div class="step-body">
      <svg width="40" height="40" viewBox="0 0 40 40"><path d="M20 8 L8 30 L32 30 Z" fill="none" stroke="#0b2c9e" stroke-width="3"/><circle cx="20" cy="8" r="5" fill="#0b2c9e"/><circle cx="8" cy="30" r="5" fill="#0b2c9e"/><circle cx="32" cy="30" r="5" fill="#0b2c9e"/></svg>
      <b>CONNECT TO ANY SWITCH<br>IN THE COMPANY</b>
    </div>
  </div>
</section>

<section class="abs anywhere">
  <div class="anywhere-photo" role="img" aria-label="Photo of a woman working at a home desk with a cat beside her"></div>
  <div class="anywhere-panel">
    <h2>WORK FROM ANYWHERE</h2>
    <p>There are many variations of passages of Lorem Ipsum available, but the majority have suffered alteration in some form, by injected humour, or randomised words which don't look even slightly believable. If you are going to use a passage of Lorem Ipsum, you need to be sure there isn't anything embarrassing hidden in the middle of text.</p>
    <a class="btn btn-navy" href="#">READ MORE</a>
  </div>
</section>

<section class="abs faq">
  <div class="faq-decor" style="left:120px;top:40px;width:150px;height:120px" role="img" aria-label="Decorative connected-node pattern in blue tones"></div>
  <div class="faq-decor" style="left:900px;top:330px;width:180px;height:160px" role="img" aria-label="Decorative connected-node pattern in blue tones"></div>
  <h2>FAQ'S</h2>
  <div class="faq-item" style="top:140px">Sed ut perspiciatis unde omnis iste natus error sit voluptatem accusantiu?<span class="faq-toggle">›</span></div>
  <div class="faq-item" style="top:208px">Sed ut perspiciatis unde omnis iste natus error sit voluptatem accusantiu?<span class="faq-toggle">›</span></div>
  <div class="faq-item" style="top:276px">Sed ut perspiciatis unde omnis iste natus error sit voluptatem accusantiu?<span class="faq-toggle">›</span></div>
  <div class="faq-item" style="top:344px">Sed ut perspiciatis unde omnis iste natus error sit voluptatem accusantiu?<span class="faq-toggle">›</span></div>
</section>

<footer class="abs site-footer">
  <div class="brand"><span class="brand-mark"></span>CopperVale</div>
  <p class="footer-about">Sed ut perspiciatis unde omnis iste natus error sit voluptatem accusantium doloreque laudan tium, totam rem aperiam, eaque ipsa quae ab illo inve ntore veritatis et quasi architecto beatae.</p>

  <div class="abs footer-col" style="left:470px;top:90px">
    <h3>CONTACT US</h3>
    <ul class="contact-list">
      <li><svg width="16" height="20" viewBox="0 0 16 20"><path d="M8 1a7 7 0 0 1 7 7c0 5-7 11-7 11S1 13 1 8a7 7 0 0 1 7-7z" fill="none" stroke="#c7d3ff" stroke-width="2"/><circle cx="8" cy="8" r="2.5" fill="#c7d3ff"/></svg><span>CopperVale<br>330 ipsam voluptatem<br>quia voluptas</span></li>
      <li><svg width="16" height="18" viewBox="0 0 16 18"><path d="M3 1h3l2 5-2 1.5a9 9 0 0 0 4 4L11.5 9l4.5 2v3a2 2 0 0 1-2 2C7 16 1 10 1 3a2 2 0 0 1 2-2z" fill="none" stroke="#c7d3ff" stroke-width="2"/></svg><span>Phone:<br>555-0100-213</span></li>
      <li><svg width="16" height="14" viewBox="0 0 16 14"><rect x="1" y="1" width="14" height="12" fill="none" stroke="#c7d3ff" stroke-width="2"/><path d="M1 2l7 6 7-6" fill="none" stroke="#c7d3ff" stroke-width="2"/></svg><span>Email:<br>info@coppervale.example</span></li>
    </ul>
  </div>

  <div class="abs footer-col" style="left:764px;top:90px">
    <h3>SIGN UP TO RECEIVE EMAIL</h3>
    <p class="sub">Excepteur sint occaecat cupidatat non proident, sunt in culpa qui officia deserunt mollit.</p>
    <div class="email-field">Enter Email</div>
    <a class="btn btn-solid" href="#">SUBSCRIBE</a>
  </div>

  <div class="footer-bottom">
    <div class="socials"><span></span><span></span><span></span><span></span></div>
    <div class="copyright">Copyright © CopperVale 2021. All rights reserved. | Privacy Policy</div>
  </div>
</footer>

</body>
</html>
```